plume du matin stationary project
Business cards, letterheads, envelopes
Project: plume du matin stationary project
plume du matin stationary project - Financial Services
Creative Brief
Bright & Fun-filled
Glen Marrish
Financial Adviser
GPO Box 7185 BRISBANE QLD 4001
glen@plumedumatin.com.au
www.plumedumatin.com.au
ABN 82 407 913 566
Qualification next to Name to read in smaller writing: Diploma of Financial Services plume du matin logo on front (no tagline). Also need to include the following in small writing perhaps going up the side of the card or along the bottom: plume du matin pty ltd is an Authorised Representative of Tamborine Financial Services Pty Ltd AFSL 718 260
plume du matin Logo with tagline Specialising in Personal & Business Risk Protection Strategies (all centred)

```html
<!DOCTYPE html>
<html lang="en">
<head>
<meta charset="utf-8">
<title>plume du matin — stationery</title>
<link rel="stylesheet" href="https://fonts.googleapis.com/css2?family=Questrial&family=Arimo:wght@400;700&display=swap">
<style>
  :root {
    --backdrop: #2e2e30;
    --paper: #ffffff;
    --paper-shade: #f1f1f1;
    --wine: #8c1c22;
    --wine-deep: #6e1217;
    --charcoal: #2b2b2d;
    --ink: #3a3a3a;
    --ink-soft: #8a8a8a;
    --ghost: #ececec;
  }
  * { box-sizing: border-box; margin: 0; padding: 0; }
  html, body { width: 1200px; height: 799px; overflow: hidden; }
  body {
    background: var(--backdrop);
    font-family: "Arimo", Arial, sans-serif;
    color: var(--ink);
    position: relative;
  }

  /* brand lockup */
  .brand { display: flex; align-items: center; gap: 6px; }
  .brand-dot {
    border: 2px solid var(--wine);
    border-radius: 50%;
    flex: none;
  }
  .brand-name {
    font-family: "Questrial", Arial, sans-serif;
    color: var(--charcoal);
    letter-spacing: -0.5px;
    white-space: nowrap;
  }
  .brand.on-dark .brand-dot { border-color: var(--paper); }
  .brand.on-dark .brand-name { color: var(--paper); }

  /* letterhead */
  .letterhead {
    position: absolute; left: 72px; top: 36px;
    width: 528px; height: 732px;
    background: var(--paper);
    overflow: hidden;
  }
  .letterhead .brand { position: absolute; left: 44px; top: 46px; }
  .letterhead .brand-dot { width: 34px; height: 34px; }
  .letterhead .brand-name { font-size: 27px; }
  .letterhead .ghost-mark {
    position: absolute; left: 120px; top: 360px;
    width: 300px; height: 300px; border-radius: 50%;
    background: var(--ghost); opacity: .55;
  }
  .letter-body {
    position: absolute; left: 44px; top: 150px; width: 430px;
    font-size: 7.6px; line-height: 1.45; color: var(--ink);
  }
  .letter-body p { margin-bottom: 11px; }
  .recipient { margin-bottom: 34px !important; }
  .signature-space {
    width: 90px; height: 30px; margin: 6px 0 0;
    background: linear-gradient(90deg, #e4e4e4, #f6f6f6);
  }
  .letter-footer {
    position: absolute; left: 0; bottom: 0; width: 100%; height: 26px;
    background: var(--wine);
    display: flex; align-items: center; justify-content: center; gap: 14px;
    font-size: 6.2px; color: var(--paper); letter-spacing: .2px;
  }

  /* business cards */
  .card {
    position: absolute; width: 166px; height: 98px;
    border-radius: 5px; overflow: hidden;
  }
  .card-white { background: linear-gradient(160deg, var(--paper), var(--paper-shade)); }
  .card-wine { background: var(--wine); }
  .card-dark { background: var(--charcoal); }
  .card.front { left: 642px; top: 32px; }
  .card.wine-back { left: 824px; top: 32px; }
  .card.white-back { left: 642px; top: 144px; }
  .card.dark-back { left: 824px; top: 144px; }

  .card.front .brand { position: absolute; left: 10px; top: 12px; gap: 4px; }
  .card .brand-dot { width: 14px; height: 14px; border-width: 1.5px; }
  .card .brand-name { font-size: 12px; }
  .card-contact {
    position: absolute; left: 10px; top: 44px;
    font-size: 4.6px; line-height: 1.5; color: var(--ink);
  }
  .card-person {
    position: absolute; right: 10px; top: 44px; text-align: right;
    font-size: 4.6px; line-height: 1.5; color: var(--ink-soft);
  }
  .card-person .person-name { font-size: 7px; font-weight: 700; color: var(--charcoal); }
  .card-legal {
    position: absolute; left: 10px; right: 10px; bottom: 6px;
    font-size: 3.4px; color: var(--ink-soft);
  }
  .card-centered {
    display: flex; flex-direction: column; align-items: center; justify-content: center;
    gap: 6px; height: 100%;
  }
  .card-centered .brand-name { font-size: 13px; }
  .tagline {
    font-size: 5px; text-align: center; line-height: 1.4; color: var(--ink);
  }
  .on-dark-text { color: var(--paper); }

  /* envelopes */
  .envelope {
    position: absolute; left: 636px; width: 516px;
    background: var(--paper); overflow: hidden;
  }
  .envelope.back { top: 288px; height: 214px; }
  .envelope.back svg { position: absolute; inset: 0; }
  .envelope.back .seal {
    position: absolute; left: 243px; top: 58px;
    width: 30px; height: 30px; border-radius: 50%;
    border: 2px solid var(--paper);
  }
  .envelope.back .seal-low {
    position: absolute; left: 245px; top: 120px;
    width: 26px; height: 26px; border-radius: 50%;
    border: 2px solid var(--wine);
  }
  .envelope.front { top: 528px; height: 246px; }
  .envelope.front .brand { position: absolute; left: 28px; top: 28px; }
  .envelope.front .brand-dot { width: 26px; height: 26px; }
  .envelope.front .brand-name { font-size: 22px; }
  .envelope.front .return-tag {
    position: absolute; left: 62px; top: 60px;
    font-size: 4.4px; color: var(--ink-soft); letter-spacing: .6px;
  }
  .envelope.front .ghost-mark {
    position: absolute; right: 30px; top: 90px;
    width: 130px; height: 130px; border-radius: 50%;
    background: var(--ghost); opacity: .7;
  }
  .envelope.front .base-band {
    position: absolute; left: 0; bottom: 0; width: 100%; height: 10px;
    background: var(--wine);
  }
</style>
</head>
<body>

  <!-- Letterhead -->
  <section class="letterhead">
    <div class="brand">
      <span class="brand-dot"></span>
      <span class="brand-name">plume du matin</span>
    </div>
    <div class="ghost-mark"></div>
    <div class="letter-body">
      <p class="recipient">Someone Somebody<br>100 Long St<br>Brisbane, Australia</p>
      <p>Dear Someone Somebody,</p>
      <p>Lorem ipsum dolor sit amet, consectetuer adipiscing elit, sed diam nonummy nibh euismod tincidunt ut laoreet dolore magna aliquam erat volutpat. Ut wisi enim ad minim veniam, quis nostrud exerci tation ullamcorper suscipit lobortis nisl ut aliquip ex ea commodo consequat. Duis autem vel eum iriure dolor in hendrerit in vulputate velit esse molestie consequat.</p>
      <p>Lorem ipsum dolor sit amet, consectetuer adipiscing elit, sed diam nonummy nibh euismod tincidunt ut laoreet dolore magna aliquam erat volutpat. Ut wisi enim ad minim veniam, quis nostrud exerci tation ullamcorper suscipit lobortis nisl ut aliquip ex ea commodo consequat. Duis autem vel eum iriure dolor in hendrerit in vulputate velit esse molestie consequat.</p>
      <p>Lorem ipsum dolor sit amet, consectetuer adipiscing elit, sed diam nonummy nibh euismod tincidunt ut laoreet dolore magna aliquam erat volutpat. Ut wisi enim ad minim veniam, quis nostrud exerci tation ullamcorper suscipit lobortis nisl ut aliquip ex ea commodo consequat. Duis autem vel eum iriure dolor in hendrerit in vulputate velit esse molestie consequat.</p>
      <p>Yours Sincerely<br>Glen Marrish</p>
      <div class="signature-space" role="img" aria-label="Handwritten signature"></div>
    </div>
    <footer class="letter-footer">
      <span>GPO Box 7185 BRISBANE QLD 4001</span>
      <span>glen@plumedumatin.com.au</span>
      <span>www.plumedumatin.com.au</span>
      <span>ABN 82 407 913 566</span>
    </footer>
  </section>

  <!-- Business card: front -->
  <div class="card card-white front">
    <div class="brand">
      <span class="brand-dot"></span>
      <span class="brand-name">plume du matin</span>
    </div>
    <div class="card-contact">
      GPO Box 7185<br>BRISBANE QLD 4001<br>glen@plumedumatin.com.au<br>www.plumedumatin.com.au<br>ABN 82 407 913 566
    </div>
    <div class="card-person">
      <div class="person-name">Glen Marrish</div>
      Diploma of Financial Services<br>Financial Adviser
    </div>
    <div class="card-legal">plume du matin pty ltd is an Authorised Representative of Tamborine Financial Services Pty Ltd AFSL 718 260</div>
  </div>

  <!-- Business card: wine back -->
  <div class="card card-wine wine-back">
    <div class="card-centered">
      <div class="brand on-dark">
        <span class="brand-dot"></span>
        <span class="brand-name">plume du matin</span>
      </div>
      <p class="tagline on-dark-text">Specialising in Personal &amp; Business Risk<br>Protection Strategies</p>
    </div>
  </div>

  <!-- Business card: white back -->
  <div class="card card-white white-back">
    <div class="card-centered">
      <p class="tagline">Specialising in Personal &amp; Business Risk<br>Protection Strategies</p>
    </div>
  </div>

  <!-- Business card: dark back -->
  <div class="card card-dark dark-back">
    <div class="card-centered">
      <p class="tagline on-dark-text">Specialising in Personal &amp; Business Risk<br>Protection Strategies</p>
    </div>
  </div>

  <!-- Envelope: back with flap -->
  <div class="envelope back">
    <svg width="516" height="214" viewBox="0 0 516 214" aria-hidden="true">
      <path d="M0 0 L516 0 L516 40 L258 118 L0 40 Z" fill="var(--wine)"/>
      <path d="M0 40 L258 118 L516 40" fill="none" stroke="#d9d9d9" stroke-width="1"/>
      <path d="M0 214 L240 120 M516 214 L276 120" stroke="#e2e2e2" stroke-width="1"/>
    </svg>
    <span class="seal"></span>
    <span class="seal-low"></span>
  </div>

  <!-- Envelope: front -->
  <div class="envelope front">
    <div class="brand">
      <span class="brand-dot"></span>
      <span class="brand-name">plume du matin</span>
    </div>
    <div class="return-tag">SPECIALISING IN RISK PROTECTION</div>
    <div class="ghost-mark"></div>
    <div class="base-band"></div>
  </div>

</body>
</html>
```